Letterhead designs for Property Management firm

Would like to see some different letterhead/envelope designs We are a residential property management company. We would like to see designs that utilize blue/grays/black

```html
<!DOCTYPE html>
<html lang="en">
<head>
<meta charset="utf-8">
<title>Harborline Property Management – Letterhead</title>
<link rel="stylesheet" href="https://fonts.googleapis.com/css2?family=Arimo:wght@400;700&display=swap">
<style>
  :root {
    --backdrop: #2a2b2e;
    --paper: #ffffff;
    --paper-shade: #f3f3f4;
    --brand-blue: #1f56b0;
    --ink: #4a4a4c;
    --ink-strong: #3b3b3d;
    --signature-tone: #d9dbe2;
  }
  * { box-sizing: border-box; margin: 0; padding: 0; }
  html, body {
    width: 1200px; height: 1200px; overflow: hidden;
    background: var(--backdrop);
    font-family: "Arimo", Arial, sans-serif;
  }
  .letterhead {
    position: absolute; left: 181px; top: 20px;
    width: 838px; height: 1160px;
    background: linear-gradient(180deg, var(--paper) 0%, var(--paper-shade) 100%);
    color: var(--ink);
  }
  .brand {
    position: absolute; left: 63px; top: 48px;
    display: flex; align-items: center; gap: 12px;
    color: var(--brand-blue); font-weight: 700;
  }
  .brand-mark { width: 22px; height: 22px; background: var(--brand-blue); }
  .brand-name { font-size: 30px; line-height: 1.1; letter-spacing: 0.5px; }
  .brand-name span { display: block; font-size: 17px; letter-spacing: 1px; }
  .contact {
    position: absolute; left: 590px; top: 55px;
    font-size: 13.5px; line-height: 17px;
  }
  .contact-lines { list-style: none; margin-top: 10px; }
  .contact-lines li { display: flex; align-items: center; gap: 6px; }
  .contact-lines svg { width: 10px; height: 10px; fill: none; stroke: var(--brand-blue); stroke-width: 1.6; }
  .letter {
    position: absolute; left: 89px; top: 268px; width: 662px;
    font-size: 13.6px; line-height: 19.8px;
  }
  .letter-date { margin-bottom: 39px; }
  .recipient { margin-bottom: 20px; }
  .recipient strong, .sign-off strong { color: var(--ink-strong); font-weight: 700; }
  .salutation { margin-bottom: 20px; }
  .letter-body p { text-align: justify; margin-bottom: 20px; }
  .sign-off { margin-top: 38px; }
  .signature {
    display: block; width: 180px; height: 20px; margin: 0 0 2px;
    background: var(--signature-tone); border-radius: 3px;
  }
</style>
</head>
<body>
  <main class="letterhead">
    <header>
      <div class="brand">
        <div class="brand-mark"></div>
        <div class="brand-name">HARBORLINE<span>PROPERTY MANAGEMENT</span></div>
      </div>
      <address class="contact" style="font-style:normal">
        Co.Street, Building/Suite 12345<br>City/State, Zip Code
        <ul class="contact-lines">
          <li><svg viewBox="0 0 10 10"><path d="M2 1 L4 3 L3 4.5 Q4.5 6.5 5.5 7 L7 6 L9 8 L7.5 9.3 Q2 8 0.8 2.5 Z"/></svg>300.555.0142</li>
          <li><svg viewBox="0 0 10 10"><rect x="1" y="2" width="8" height="6"/><path d="M1 2 L5 5.5 L9 2"/></svg>info@harborlineproperty.com</li>
          <li><svg viewBox="0 0 10 10"><circle cx="5" cy="5" r="4"/><path d="M1 5 H9 M5 1 Q2 5 5 9 M5 1 Q8 5 5 9"/></svg>www.harborlineproperty.com</li>
        </ul>
      </address>
    </header>

    <section class="letter">
      <p class="letter-date">January 1, 2050</p>
      <p class="recipient"><strong>Daniel Reeve</strong><br>Managing Director<br>Co.Street, Building/Suite<br>City/State, Zip Code</p>
      <p class="salutation">Dear Thomas Avery,</p>
      <div class="letter-body">
        <p>Lorem ipsum dolor sit amet, consectetuer adipiscing elit, sed diam nonummy nibh euismod tincidunt ut laoreet dolore magna aliquam erat volutpat. Ut wisi enim ad minim veniam, quis nostrud exerci tation ullamcorper suscipit lobortis nisl ut aliquip ex ea commodo consequat. Duis dolore te feugait nulla facilisi. Nam liber tempor cum soluta nobis eleifend option congue nihil imperdiet doming id quod mazim placerat facer possim assum. Lorem ipsum dolor sit amet, consectetuer adipiscing elit, sed diam nonummy nibh euismod tincidunt ut laoreet dolore magna aliquam erat volutpat. Ut wisi enim ad minim veniam, quis nostrud exerci tation ullamcorper suscipit lobortis nisl ut aliquip ex ea commodo consequat.</p>
        <p>Consectetuer adipiscing elit, sed diam nonummy nibh euismod tincidunt ut laoreet dolore magna aliquam erat volutpat. Ut wisi enim ad minim veniam, quis nostrud exerci tation ullamcorper suscipit lobortis nisl ut aliquip ex ea commodo consequat. Consectetuer adipiscing elit, sed diam nonummy nibh euismod tincidunt ut laoreet dolore magna aliquam erat volutpat. Ut wisi enim ad minim veniam, quis nostrud exerci tation ullamcorper suscipit lobortis nisl ut aliquip ex ea commodo consequat.</p>
        <p>Duis dolore te feugait nulla facilisi. Nam liber tempor cum soluta nobis eleifend option congue nihil imperdiet doming id quod mazim placerat facer possim assum.Duis dolore te feugait nulla facilisi. Nam liber tempor cum soluta nobis eleifend option congue nihil imperdiet doming id quod mazim placerat facer possim assum.</p>
      </div>
      <div class="sign-off">
        Sincerely Yours,
        <span class="signature" role="img" aria-label="Handwritten signature of Martin Hale"></span>
        <strong>Authorized Managing Director</strong><br>Your Company Name
      </div>
    </section>
  </main>
</body>
</html>
```